Business Card Design

I would like a new business card that incorporates the new colors and font of the attached MDP4x10.pdf file of our new sign (latte & luxurious red from Halcott Brennan colors) with the logo from the old business card (file name is New2014.pdf). You can remove the phrases from the old card, and just use the contact info provided above. Please let me know if you have any questions.

Industry/Entity Type

Business

Contact Information for Business Card

Marcus Dean Pryor, LLC
Real Estate Attorney
482 Alder Street
Cedar Hollow, GA 30599
(O) 555-302-4187
(C) 555-719-2630
marcus@mdpcounsel.com
mdpcounsel.com

```html
<!DOCTYPE html>
<html lang="en">
<head>
<meta charset="utf-8">
<title>Marcus Dean Pryor, LLC — Business Card</title>
<link rel="stylesheet" href="https://fonts.googleapis.com/css2?family=Arvo:wght@400;700&display=swap">
<style>
  :root {
    --stage: #000000;
    --luxurious-red: #a8474f;
    --latte: #f3e7da;
    --ink-blue: #3f506f;
    --accent-red: #a3414a;
  }
  * { margin: 0; padding: 0; box-sizing: border-box; }
  html, body {
    width: 1200px;
    height: 675px;
    overflow: hidden;
    background: var(--stage);
  }
  .canvas {
    position: relative;
    width: 1200px;
    height: 675px;
  }
  .card {
    position: absolute;
    left: 312px;
    top: 174px;
    width: 574px;
    height: 324px;
    background: var(--luxurious-red);
    padding: 13px 14px 14px 13px;
    font-family: "Arvo", Georgia, serif;
  }
  .card-face {
    position: relative;
    width: 100%;
    height: 100%;
    background: var(--latte);
  }
  .brand-name {
    position: absolute;
    left: 36px;
    top: 138px;
    width: 202px;
    text-align: center;
    font-size: 16px;
    font-weight: 400;
    color: var(--accent-red);
    white-space: nowrap;
  }
  .divider {
    position: absolute;
    left: 272px;
    top: 62px;
    width: 2px;
    height: 184px;
    background: var(--ink-blue);
  }
  .details {
    position: absolute;
    left: 330px;
    top: 60px;
  }
  .firm-name {
    font-size: 13px;
    font-weight: 700;
    color: var(--ink-blue);
    letter-spacing: 0.3px;
    text-transform: uppercase;
  }
  .firm-role {
    margin-top: 7px;
    font-size: 13px;
    color: var(--accent-red);
  }
  .contact-list {
    list-style: none;
    margin-top: 21px;
  }
  .contact-item {
    position: relative;
    padding-left: 27px;
    height: 22.7px;
    line-height: 22.7px;
    font-size: 13px;
    color: var(--ink-blue);
    white-space: nowrap;
  }
  .contact-icon {
    position: absolute;
    left: 0;
    top: 3px;
    width: 15px;
    height: 15px;
    fill: var(--accent-red);
  }
</style>
</head>
<body>
<main class="canvas">
  <section class="card" aria-label="Business card for Marcus Dean Pryor, LLC">
    <div class="card-face">
      <p class="brand-name">Marcus Dean Pryor</p>

      <div class="divider"></div>

      <div class="details">
        <h1 class="firm-name">Marcus Dean Pryor, LLC</h1>
        <p class="firm-role">Real Estate Attorney</p>

        <ul class="contact-list">
          <li class="contact-item">
            <svg class="contact-icon" viewBox="0 0 16 16" aria-hidden="true"><path d="M3.6 1.2l2.2-.4 1.4 3.3-1.6 1.2c.8 1.8 2.2 3.2 4 4l1.2-1.6 3.3 1.4-.4 2.2c-.2.9-1 1.5-1.9 1.5C6.3 12.8 2.2 8.7 2.1 3.1c0-.9.6-1.7 1.5-1.9z"/></svg>
            555-302-4187
          </li>
          <li class="contact-item">
            <svg class="contact-icon" viewBox="0 0 16 16" aria-hidden="true"><path d="M5 1h6a1.5 1.5 0 0 1 1.5 1.5v11A1.5 1.5 0 0 1 11 15H5a1.5 1.5 0 0 1-1.5-1.5v-11A1.5 1.5 0 0 1 5 1zm0 1.6v9.4h6V2.6zm3 10.2a.7.7 0 1 0 0 1.4.7.7 0 0 0 0-1.4z"/></svg>
            555-719-2630
          </li>
          <li class="contact-item">
            <svg class="contact-icon" viewBox="0 0 16 16" aria-hidden="true"><path d="M8 1a7 7 0 1 0 0 14A7 7 0 0 0 8 1zm4.9 6.2h-2.3c-.1-1.7-.5-3.2-1.1-4.3a5.4 5.4 0 0 1 3.4 4.3zM8 2.6c.6.8 1.1 2.4 1.2 4.6H6.8C6.9 5 7.4 3.4 8 2.6zM6.5 2.9c-.6 1.1-1 2.6-1.1 4.3H3.1a5.4 5.4 0 0 1 3.4-4.3zM3.1 8.8h2.3c.1 1.7.5 3.2 1.1 4.3a5.4 5.4 0 0 1-3.4-4.3zM8 13.4c-.6-.8-1.1-2.4-1.2-4.6h2.4c-.1 2.2-.6 3.8-1.2 4.6zm1.5-.3c.6-1.1 1-2.6 1.1-4.3h2.3a5.4 5.4 0 0 1-3.4 4.3z"/></svg>
            mdpcounsel.com
          </li>
          <li class="contact-item">
            <svg class="contact-icon" viewBox="0 0 16 16" aria-hidden="true"><path d="M1 6l7-4.5L15 6v8H1zm2 .8L8 10l5-3.2L8 3.6z"/></svg>
            marcus@mdpcounsel.com
          </li>
          <li class="contact-item">
            <svg class="contact-icon" viewBox="0 0 16 16" aria-hidden="true"><path d="M8 1a4.6 4.6 0 0 0-4.6 4.6C3.4 9 8 15 8 15s4.6-6 4.6-9.4A4.6 4.6 0 0 0 8 1zm0 6.4a1.8 1.8 0 1 1 0-3.6 1.8 1.8 0 0 1 0 3.6z"/></svg>
            482 Alder Street
          </li>
          <li class="contact-item">Cedar Hollow, GA 30599</li>
        </ul>
      </div>
    </div>
  </section>
</main>
</body>
</html>
```